Web Design Project

We are an IT System Integrator. We provide Norvik 500 ERP System, CRM etc. We also provide hardware, networking servicing. Please look at www.brinquot.com.sg. They provide the same service as us. We like to redesign our web site. I will attached the color that I prefer for reference.

Our website is www.ravdu.com.sg.  It has been created about 14 years ago.  We are trying to revamp it with a new look and information.   The new website must be informative, fast.    I have attached an attachment which show the color that I prefer(brownish golden).   

Our competitor (www.brinquot.com) is carrying the same trade as us.  They have all the informations In their website that we will like to have.  Therefore I recommend you to take a look at my competitor website and have a better   
understanding on the kind of information I would like to have for my new website.

This project is guarantee to the person with the best design.  We can have it guarantee.

Target Market(s)

Corporate and companies

Industry/Entity Type

Hardware

```html
<!DOCTYPE html>
<html lang="en">
<head>
<meta charset="utf-8">
<title>Ravdu Information System</title>
<link rel="stylesheet" href="https://fonts.googleapis.com/css2?family=Arimo:wght@400;700&family=Bree+Serif&display=swap">
<style>
  :root {
    --gold: #c9a95a;
    --gold-light: #e9d7a6;
    --gold-pale: #f6efdc;
    --gold-dark: #8f6c25;
    --brown: #7a5a1b;
    --ink: #111111;
    --white: #ffffff;
    --link-blue: #1c5d9e;
    --sky: #1f8fe0;
    --sky-pale: #dcebf7;
    --login-card: #f3f4f4;
    --login-foot: #dde2e3;
    --login-btn: #4dbde3;
  }
  * { box-sizing: border-box; margin: 0; padding: 0; }
  html, body { width: 915px; height: 1200px; overflow: hidden; }
  body {
    position: relative;
    background: var(--white);
    font-family: "Arimo", Arial, sans-serif;
    color: var(--ink);
  }

  /* Header */
  .site-header { position: absolute; left: 0; top: 0; width: 915px; height: 315px; }
  .site-header__bg { position: absolute; inset: 0; }
  .brand {
    position: absolute; left: 55px; top: 0; width: 283px; height: 196px;
    clip-path: polygon(0 0, 100% 0, 100% 85%, 50% 100%, 0 85%);
    background: linear-gradient(180deg, #b8964a 0%, #e6d3a0 55%, #c7a65c 100%);
    display: flex; flex-direction: column; align-items: center; justify-content: center;
    padding-bottom: 24px;
  }
  .brand__name {
    font-size: 44px; font-weight: 700; color: var(--brown); letter-spacing: 1px;
    display: flex; align-items: center; gap: 10px;
  }
  .brand__dot { width: 22px; height: 22px; border-radius: 50%; background: var(--brown); }
  .brand__tagline { margin-top: 10px; font-size: 17px; color: #3a2c10; }
  .phone { position: absolute; left: 78px; top: 210px; font-size: 24px; color: var(--white); }
  .hero-globe {
    position: absolute; left: 575px; top: -5px; width: 270px; height: 270px; border-radius: 50%;
    background: radial-gradient(circle at 40% 40%, #fff3ec 0%, #f7a07d 40%, #ec4e1c 75%, #f8c7b0 100%);
  }

  /* Navigation */
  .main-nav {
    position: absolute; left: 30px; top: 263px; width: 858px; height: 48px; border-radius: 8px;
    background: linear-gradient(180deg, #e2c97f 0%, #c6a352 55%, #a48236 100%);
    box-shadow: 2px 3px 3px rgba(60, 40, 0, .45);
  }
  .nav-list {
    list-style: none; display: flex; justify-content: center; align-items: center; height: 100%;
    font-size: 12.5px; font-weight: 700; color: var(--white);
  }
  .nav-list li + li::before { content: "|"; margin: 0 8px; }

  /* Profile */
  .profile {
    position: absolute; left: 55px; top: 323px; width: 800px; height: 220px;
    border-radius: 8px 8px 0 0;
    background: linear-gradient(180deg, #c4a456 0%, #dcc58c 45%, #f3e9d2 80%, #ffffff 100%);
    padding: 14px 17px 0 22px;
  }
  .profile__title { font-size: 16.5px; font-weight: 400; margin-left: 2px; margin-bottom: 9px; }
  .profile p { font-size: 12.6px; line-height: 14.5px; text-align: justify; margin-bottom: 14px; hyphens: auto; }

  /* Feature cards */
  .features { position: absolute; left: 52px; top: 549px; display: flex; gap: 11px; }
  .feature {
    position: relative; width: 193px; height: 272px; border-radius: 7px 7px 0 0;
    background: linear-gradient(180deg, #c8a85b 0%, #e7d6a9 16%, #fbf7ee 30%, #ffffff 55%, #f9f6ef 100%);
    padding: 56px 11px 0 13px;
  }
  .feature__title { position: absolute; top: 9px; left: 0; right: 0; text-align: center; font-size: 12.5px; font-weight: 400; }
  .feature__icon { position: absolute; left: 10px; top: 8px; width: 38px; height: 44px; border-radius: 4px; }
  .feature__icon--focus { background: linear-gradient(180deg, #e9b23b, #b33a1c); border-radius: 50%; left: 8px; top: 19px; width: 52px; height: 36px; }
  .feature__icon--partners { background: linear-gradient(180deg, #3a3a3a, #111); width: 34px; left: 14px; }
  .feature__icon--news { background: linear-gradient(135deg, #8c98e6, #3f4fb5); left: 14px; top: 11px; width: 44px; height: 40px; }
  .feature__icon--ledger { background: linear-gradient(135deg, #dfe8ef, #1a7fb8); left: 14px; top: 6px; width: 42px; height: 46px; }
  .feature__text { font-size: 9.2px; line-height: 14.45px; text-align: justify; }
  .feature__more { display: block; text-align: right; margin-top: 6px; font-size: 8.5px; color: var(--link-blue); text-decoration: none; }

  /* Login */
  .login-panel { position: absolute; left: 85px; top: 827px; width: 227px; height: 248px; background: linear-gradient(180deg, #b5d3df, #8fb5c6); }
  .login-card { position: absolute; left: 40px; top: 8px; width: 174px; height: 240px; background: var(--login-card); border-radius: 3px 3px 0 0; }
  .login-card__title { font-family: "Bree Serif", Georgia, serif; font-size: 15.5px; font-weight: 400; color: #3a3a3a; margin: 18px 0 0 19px; }
  .login-card__hint { font-size: 5.5px; line-height: 7px; color: #4a8aa6; margin: 6px 20px 0 19px; }
  .login-field { position: absolute; left: 20px; width: 134px; height: 26px; background: var(--white); border: 1px solid #d6dadb; border-radius: 3px; font-size: 7px; color: #8a9396; padding: 9px 0 0 12px; }
  .login-field--user { top: 77px; }
  .login-field--pass { top: 122px; letter-spacing: 1px; }
  .login-tag { position: absolute; left: 15px; width: 25px; height: 25px; background: #5d6c72; border-radius: 2px; }
  .login-tag--user { top: 85px; }
  .login-tag--pass { top: 130px; }
  .login-tag svg { display: block; margin: 6px auto 0; }
  .login-card__foot { position: absolute; left: 0; right: 0; bottom: 0; height: 73px; background: var(--login-foot); }
  .login-card__register { position: absolute; left: 41px; top: 21px; font-family: "Bree Serif", Georgia, serif; font-size: 9px; color: #555; }
  .login-card__submit { position: absolute; left: 94px; top: 14px; width: 61px; height: 25px; border-radius: 3px; background: var(--login-btn); color: var(--white); font-family: "Bree Serif", Georgia, serif; font-size: 9px; text-align: center; line-height: 25px; }

  /* Product banner */
  .product-banner { position: absolute; left: 337px; top: 828px; width: 497px; height: 247px; background: var(--white); border-bottom: 3px solid #bdbdbd; overflow: hidden; }
  .product-banner__bar {
    height: 32px; background: linear-gradient(180deg, #f2f2f2 0%, #b5b5b5 60%, #7d7d7d 100%);
    text-align: center; font-size: 17px; font-weight: 700; letter-spacing: 3px; line-height: 34px;
    color: #8e8e8e; text-shadow: 0 1px 0 #eeeeee;
  }
  .product-banner__art {
    position: absolute; left: 0; top: 32px; width: 497px; height: 212px;
    background: linear-gradient(180deg, var(--white) 0%, var(--sky-pale) 35%, #8cc3ec 60%, var(--white) 100%);
  }

  /* Footer */
  .site-footer { position: absolute; left: 0; top: 1100px; width: 915px; height: 90px; background: var(--brown); }
  .site-footer .nav-list { height: 64px; }
</style>
</head>
<body>

<header class="site-header">
  <svg class="site-header__bg" width="915" height="315" viewBox="0 0 915 315" aria-hidden="true">
    <defs>
      <linearGradient id="headerFill" x1="0" y1="0" x2="1" y2="0">
        <stop offset="0" stop-color="#b0914c"/>
        <stop offset=".5" stop-color="#a58543"/>
        <stop offset="1" stop-color="#8d6d2c"/>
      </linearGradient>
      <linearGradient id="sweep" x1="0" y1="0" x2="0" y2="1">
        <stop offset="0" stop-color="#e7d8ae"/>
        <stop offset="1" stop-color="#b79851"/>
      </linearGradient>
    </defs>
    <rect width="915" height="300" fill="url(#headerFill)"/>
    <path d="M0 130 C200 40 420 20 620 40 C760 55 860 40 915 30 L915 0 L0 0 Z" fill="url(#sweep)" opacity=".75"/>
    <path d="M0 230 C250 170 500 160 915 200 L915 300 L0 300 Z" fill="#c4a564" opacity=".5"/>
    <rect y="298" width="915" height="17" fill="#efe9dc"/>
  </svg>
  <div class="brand">
    <div class="brand__name"><span class="brand__dot"></span>Ravdu</div>
    <div class="brand__tagline">Ravdu Information System</div>
  </div>
  <div class="phone">Call: (065) 6210-4800</div>
  <div class="hero-globe" role="img" aria-label="Illustration of a glowing globe with a web address bar and cursor"></div>
</header>

<nav class="main-nav">
  <ul class="nav-list">
    <li>HOME</li><li>ABOUT US</li><li>PRODUCTS</li><li>SERVICES</li><li>LEDGRA</li><li>CLIENTELE</li><li>CLIENT SUPPORT</li><li>CONTACT US</li>
  </ul>
</nav>

<section class="profile">
  <h2 class="profile__title">Profile</h2>
  <p>Lorem ipsum dolor sit amet, consectetur adipisicing elit, sed do eiusmod tempor incididunt ut labore et dolore magna aliqua. Ut enim ad minim veniam, quis nostrud exercitation ullamco laboris nisi ut aliquip ex ea commodo consequat. Duis aute irure dolor in reprehenderit in voluptate velit esse cillum dolore eu fugiat nulla pariatur. Excepteur sint occaecat cupidatat non proident, sunt in culpa qui officia deserunt mollit anim id est laborum.</p>
  <p>Lorem ipsum dolor sit amet, consectetur adipisicing elit, sed do eiusmod tempor incididunt ut labore et dolore magna aliqua. Ut enim ad minim veniam, quis nostrud exercitation ullamco laboris nisi ut aliquip ex ea commodo consequat. Duis aute irure dolor in reprehenderit in voluptate velit esse cillum dolore eu fugiat nulla pariatur. Excepteur sint occaecat cupidatat non proident, sunt in culpa qui officia deserunt mollit anim id est laborum</p>
</section>

<section class="features">
  <article class="feature">
    <div class="feature__icon feature__icon--focus" role="img" aria-label="Round customer focus badge illustration"></div>
    <h3 class="feature__title">Customer Focus</h3>
    <p class="feature__text">Lorem ipsum dolor sit amet, consectetur adipisicing elit, sed do eiusmod tempor incididunt ut labore et dolore magna aliqua. Ut enim ad minim veniam, quis nostrud exercitation ullamco laboris nisi ut aliquip ex ea commodo consequat. Duis aute irure dolor in reprehenderit in voluptate velit esse cillum dolore eu fugiat nulla pariatur. Excepteur sint occaecat cupidatat non proident, sunt in culpa qui officia deserunt mollit anim id est laborum.</p>
    <a class="feature__more" href="#">READ MORE</a>
  </article>
  <article class="feature">
    <div class="feature__icon feature__icon--partners" role="img" aria-label="Silhouette of two business partners shaking hands"></div>
    <h3 class="feature__title">Partners</h3>
    <p class="feature__text">Lorem ipsum dolor sit amet, consectetur adipisicing elit, sed do eiusmod tempor incididunt ut labore et dolore magna aliqua. Ut enim ad minim veniam, quis nostrud exercitation ullamco laboris nisi ut aliquip ex ea commodo consequat. Duis aute irure dolor in reprehenderit in voluptate velit esse cillum dolore eu fugiat nulla pariatur. Excepteur sint occaecat cupidatat non proident, sunt in culpa qui officia deserunt mollit anim id est laborum.</p>
    <a class="feature__more" href="#">READ MORE</a>
  </article>
  <article class="feature">
    <div class="feature__icon feature__icon--news" role="img" aria-label="Blue news feed graphic"></div>
    <h3 class="feature__title">News</h3>
    <p class="feature__text">Lorem ipsum dolor sit amet, consectetur adipisicing elit, sed do eiusmod tempor incididunt ut labore et dolore magna aliqua. Ut enim ad minim veniam, quis nostrud exercitation ullamco laboris nisi ut aliquip ex ea commodo consequat. Duis aute irure dolor in reprehenderit in voluptate velit esse cillum dolore eu fugiat nulla pariatur. Excepteur sint occaecat cupidatat non proident, sunt in culpa qui officia deserunt mollit anim id est laborum.</p>
    <a class="feature__more" href="#">READ MORE</a>
  </article>
  <article class="feature">
    <div class="feature__icon feature__icon--ledger" role="img" aria-label="Software product box"></div>
    <h3 class="feature__title">LEDGRA</h3>
    <p class="feature__text">Lorem ipsum dolor sit amet, consectetur adipisicing elit, sed do eiusmod tempor incididunt ut labore et dolore magna aliqua. Ut enim ad minim veniam, quis nostrud exercitation ullamco laboris nisi ut aliquip ex ea commodo consequat. Duis aute irure dolor in reprehenderit in voluptate velit esse cillum dolore eu fugiat nulla pariatur. Excepteur sint occaecat cupidatat non proident, sunt in culpa qui officia deserunt mollit anim id est laborum.</p>
    <a class="feature__more" href="#">READ MORE</a>
  </article>
</section>

<section class="login-panel">
  <div class="login-card">
    <h3 class="login-card__title">Login Form</h3>
    <p class="login-card__hint">Fill out the form below to login to my super awesome imaginary control panel.</p>
    <div class="login-field login-field--user">Username</div>
    <div class="login-field login-field--pass">••••••••</div>
    <div class="login-card__foot">
      <span class="login-card__register">Register</span>
      <span class="login-card__submit">Sign In</span>
    </div>
  </div>
  <div class="login-tag login-tag--user">
    <svg width="12" height="13" viewBox="0 0 12 13" aria-hidden="true"><circle cx="6" cy="3.5" r="3" fill="#fff"/><path d="M0 13 C0 8 12 8 12 13 Z" fill="#fff"/></svg>
  </div>
  <div class="login-tag login-tag--pass">
    <svg width="12" height="13" viewBox="0 0 12 13" aria-hidden="true"><path d="M3 6 V4 a3 3 0 0 1 6 0 V6" stroke="#fff" stroke-width="1.6" fill="none"/><rect x="1" y="6" width="10" height="7" rx="1" fill="#fff"/></svg>
  </div>
</section>

<section class="product-banner">
  <div class="product-banner__bar">LEDGRA</div>
  <div class="product-banner__art" role="img" aria-label="Product illustration: row of LEDGRA software boxes on a blue sweeping background"></div>
</section>

<footer class="site-footer">
  <ul class="nav-list">
    <li>HOME</li><li>ABOUT US</li><li>PRODUCTS</li><li>SERVICES</li><li>LEDGRA</li><li>CLIENTELE</li><li>CLIENT SUPPORT</li><li>CONTACT US</li>
  </ul>
</footer>

</body>
</html>
```